Recruitment Agency in Texas, needs a stand out header letter

Our colours are red and grey and can be found on our website
just my logo will be sufficient and address...

Target Market(s)

Engineering Manufacturing

Colors
0094D4
00A9DD
6FCCEA
C7EBF8
E9F6FB
EB3D1F
EC4F4E
F09395
F8D3D4
FCEDEE

Requirements
Must have
• use colors red and grey
Should not have
• Please use same colors and font as my logo. My website is kelbrantstaffing.net

```html
<!DOCTYPE html>
<html lang="en">
<head>
<meta charset="utf-8">
<title>KelbrantStaffing Letterhead</title>
<link href="https://fonts.googleapis.com/css2?family=Arimo:wght@400;700&display=swap" rel="stylesheet">
<style>
  :root {
    --brand-red: #d4202a;
    --brand-grey: #63666a;
    --text-grey: #4a4c50;
    --paper: #f4f5f6;
    --backdrop: #dcdde0;
  }
  * { margin: 0; padding: 0; box-sizing: border-box; }
  html, body { width: 1200px; height: 1141px; overflow: hidden; }
  body {
    background: var(--backdrop);
    font-family: "Arimo", Arial, sans-serif;
    color: var(--text-grey);
  }
  .letterhead {
    position: absolute;
    left: 210px; top: 22px;
    width: 780px; height: 1096px;
    background: var(--paper);
    box-shadow: 0 2px 10px rgba(0,0,0,0.15);
  }
  .brand-name {
    position: absolute;
    left: 56px; top: 90px;
    font-size: 27px; font-weight: 700;
    letter-spacing: -1.2px;
    color: var(--brand-red);
  }
  .office {
    position: absolute;
    left: 554px; top: 55px;
    font-size: 11px; line-height: 14px;
    color: var(--text-grey);
  }
  .office .contacts { margin-top: 5px; list-style: none; }
  .office .contacts li { display: flex; align-items: center; gap: 6px; }
  .office svg { width: 9px; height: 9px; fill: var(--brand-red); flex: none; }
  .salutation {
    position: absolute;
    left: 58px; top: 274px;
    font-size: 18.5px; font-weight: 400;
    color: var(--text-grey);
  }
  .letter-body {
    position: absolute;
    left: 58px; top: 330px;
    width: 664px;
    font-size: 11.2px; line-height: 16.8px;
    text-align: justify;
  }
  .letter-body p + p { margin-top: 17px; }
  .closing {
    position: absolute;
    left: 58px; top: 697px;
    font-size: 11.2px;
  }
  .signature {
    position: absolute;
    left: 52px; top: 566px; top: 732px;
    width: 226px; height: 62px;
    background: linear-gradient(90deg, #e4e5e7, #eceded);
  }
  .footer-band {
    position: absolute;
    left: 0; top: 1050px;
    width: 100%; height: 18px;
    display: flex; gap: 3px;
  }
  .footer-band .web {
    flex: 0 0 638px;
    background: var(--brand-red);
    color: #fff;
    font-size: 10px; letter-spacing: 5px;
    display: flex; align-items: center; justify-content: center;
    padding-left: 0;
  }
  .footer-band .accent { flex: 1; background: var(--brand-grey); }
</style>
</head>
<body>
  <main class="letterhead">
    <div class="brand-name">KelbrantStaffing</div>

    <address class="office">
      <div>Houston Office</div>
      <div>48 Larkspur Plaza Houston,</div>
      <ul class="contacts">
        <li><svg viewBox="0 0 10 10"><path d="M2 0.5 L3.6 2.6 L2.8 3.6 Q4 6 6.4 7.2 L7.4 6.4 L9.5 8 L8.4 9.5 Q2 8.6 0.5 1.6 Z"/></svg>(+1) 832-555-0186</li>
        <li><svg viewBox="0 0 10 10"><rect x="2.5" y="0.5" width="5" height="3"/><rect x="0.5" y="3.5" width="9" height="4.5" rx="0.8"/><rect x="2.5" y="7" width="5" height="2.5"/></svg>832-555-0187</li>
        <li><svg viewBox="0 0 10 10"><rect x="0.5" y="2" width="9" height="6.5"/><path d="M0.5 2 L5 5.5 L9.5 2" stroke="#f4f5f6" stroke-width="0.9" fill="none"/></svg>info@kelbrantstaffing.net</li>
      </ul>
    </address>

    <h1 class="salutation">Dear Mr. Harlow,</h1>

    <section class="letter-body">
      <p>Lorem ipsum dolor sit amet, consectetur adipiscing elit. Donec orci purus, luctus vitae dignissim eu, iaculis sed purus. Vivamus faucibus, ipsum nec aliquet viverra, leo mauris condimentum ligula, sit amet sagittis enim ligula quis arcu. Nam egestas tortor id nisi porttitor mattis. In tortor ante, ultricies in suscipit a, tempus non massa. Vivamus et auctor mi. Fusce vel massa nulla. Phasellus nec eros mauris, et scelerisque orci.</p>
      <p>Donec malesuada orci vitae nulla accumsan porta a id massa. Quisque accumsan iaculis magna sit amet fringilla. Maecenas consequat, magna eget tincidunt semper, odio nibh rutrum mi, id feugiat ante nisi eu risus. Vestibulum nunc orci, rhoncus a placerat in, ultricies in mi. Cras mattis varius eros, vel fringilla nisi suscipit eget. Quisque scelerisque sagittis nulla at porttitor.</p>
      <p>Sed id augue vitae urna euismod commodo aliquet a quam. Pellentesque arcu velit, cursus et malesuada ut, consequat et diam. Nullam erat sem, rhoncus id ullamcorper vitae, rhoncus et arcu. In ultricies ultricies nulla, ut rutrum nisi iaculis at. Donec eu magna a metus ornare faucibus. Fusce aliquet faucibus ultricies. Morbi semper, est id tincidunt gravida, sem arcu adipiscing lacus, ac bibendum nulla leo eu purus. Quisque nec diam sed risus consectetur a ccumsan quis quis nibh. Vestibulum id purus lorem.</p>
      <p>It is a long established fact that a reader will be distracted by the readable content of a page when looking at its layout. The point of using Lorem Ipsum is that it has a more-or-less normal distribution of letters, as opposed to using 'Content here, content here', making it look like readable English. Many desktop publishing packages</p>
      <p>ada ut, consequat et diam. Nullam erat sem, rhoncus id ullamcorper vitae, rhoncus et arcu. In ultricies ultricies nulla, ut rutrum nisi iaculis at. Donec eu magna a metus ornare faucibus. Fusce aliquet faucibus ultricies. Morbi semper,</p>
    </section>

    <div class="closing">Sincerely,</div>
    <div class="signature" role="img" aria-label="Handwritten signature of the sender"></div>

    <footer class="footer-band">
      <div class="web">www.KelbrantStaffing.net</div>
      <div class="accent"></div>
    </footer>
  </main>
</body>
</html>
```